Mock up Blog Design for midwife that works in a hospital setting

We are looking to have a design created for a midwife. This blog will be used to share information or experiences related to pregnancy, child birth and motherhood with its readership. It should convey a feeling of warmth and security to women who are looking for a partner in the birthing processes.

We are asking you to design the layout, not code it up. This is a concept project only.

NOtes from the midwife

​So I'm just going to put in links to a few blogs and say what I like and don't like about each one:

rosalindpeverell.com.au/blog/

I like how there is a colorful background that has to do with her books; maybe mine could have a background with baby stuff in the background. It's also nice how there's an index of recent postings with the subject listed and how the postings are sorted by date, all on the same page.

www.steadybottlebrigade.com

I like that this one is set up like a website with tabs for resources, a bio, reader comments, etc.

cradlecorner.tendrilfoundation.org

This blog has a very calming color scheme, which is welcoming. I like that there's a picture for every posting, and that at the bottom of the posting there is a little glossary with the subjects that are covered in the posting. Also, I like the way that the date of each blog is done.

bellyhumourhub.blogspot.com

This one is really funny, and similar in intention to the one that I want to do. I like that she has a glossary of medical terms so that readers can look them up.

General comments:
I'm not sure how much DKWH wants their logo on my blog or in the blog name...
I would like to be able to vet comments before they appear on the blog, so that if there's an inappropriate one, I can screen it out.
I would also like to be able to see how many people have viewed the site.
Updates

Target Market(s)

Pregnant mothers, new moms, hopeful moms

Industry/Entity Type

Hospital

Requirements
Must have
• Incorporation of the logo and at least one of the photographs that will be provided In the header
Should not have
• Should not look canned, rigid or boxy.

```html
<!DOCTYPE html>
<html lang="en">
<head>
<meta charset="utf-8">
<title>Dawnlight Midwifery – Blog</title>
<link href="https://fonts.googleapis.com/css2?family=Open+Sans:wght@300;400;600;700;800&display=swap" rel="stylesheet">
<style>
  :root{
    --pink:#d6508e;
    --pink-hero:#d2588f;
    --teal:#2e5566;
    --ink:#3f3f3f;
    --muted:#9a9a9a;
    --line:#e4e4e4;
    --paper:#ffffff;
    --backdrop:#f1f1f1;
    --social-1:#5fa9d6;
    --social-2:#d2588f;
    --social-3:#4d6fa8;
    --social-4:#e0664f;
  }
  *{box-sizing:border-box;margin:0;padding:0}
  html,body{width:1200px;height:1000px;overflow:hidden}
  body{background:var(--backdrop);font-family:"Open Sans",sans-serif;color:var(--ink)}
  .site{position:absolute;left:240px;top:0;width:720px;height:1000px;background:var(--paper);overflow:hidden}

  /* header */
  .brand{position:absolute;left:30px;top:34px;display:flex;align-items:center;gap:12px}
  .brand-dot{width:34px;height:34px;border-radius:50%;background:var(--pink)}
  .brand-name{font-size:34px;font-weight:400;color:var(--teal);line-height:1}
  .brand-sub{font-size:11px;letter-spacing:4px;color:var(--teal);margin-top:4px}
  .social{position:absolute;right:26px;top:128px;display:flex;gap:5px}
  .social span{width:34px;height:34px;display:block}
  .social span:nth-child(1){background:var(--social-1)}
  .social span:nth-child(2){background:var(--social-2)}
  .social span:nth-child(3){background:var(--social-3)}
  .social span:nth-child(4){background:var(--social-4)}
  .nav{position:absolute;left:250px;top:170px;display:flex;gap:20px;font-size:12.5px;color:#6a6a6a}
  .nav .active{color:var(--pink)}
  .nav .contact{display:flex;align-items:center;gap:6px;border-left:1px solid var(--line);padding-left:14px}

  /* hero */
  .hero-photo{position:absolute;left:0;top:200px;width:470px;height:270px;background:linear-gradient(135deg,#e9e6e4,#b9483f 55%,#4b4f5c)}
  .hero-quote{position:absolute;left:470px;top:200px;width:250px;height:345px;background:var(--pink-hero);color:#fff;padding:34px 28px}
  .hero-quote p{font-size:31px;font-weight:700;line-height:1.13}
  .hero-quote cite{display:block;margin-top:40px;font-style:normal;font-size:12px}

  /* posts */
  .post{position:absolute;left:26px;width:420px}
  .post-title{font-size:31px;font-weight:300;color:var(--pink);line-height:1.1}
  .post-meta{display:flex;gap:26px;font-size:8.5px;text-transform:uppercase;color:var(--muted);margin:10px 0 12px}
  .post-body{font-size:10.5px;line-height:1.45;color:var(--ink)}
  .post-body a{color:var(--pink);text-decoration:none}
  .post-one{top:488px}
  .post-two{top:818px}
  .gallery{position:absolute;left:26px;top:700px;display:flex;gap:12px}
  .gallery div{width:132px;height:100px}
  .g1{background:linear-gradient(180deg,#b7d3e6,#3d7fa6)}
  .g2{background:linear-gradient(135deg,#e8ecef,#5d8ba8)}
  .g3{background:linear-gradient(135deg,#f2f2f2,#a93442)}

  /* sidebar */
  .sidebar{position:absolute;left:490px;top:560px;width:210px;border-left:1px solid var(--line);padding-left:18px;height:440px}
  .search{display:flex;height:32px;margin-top:26px}
  .search-field{flex:1;border:1px solid var(--line);font-size:9px;color:#bbb;padding:10px}
  .search-btn{width:32px;background:#bdbdbd;display:flex;align-items:center;justify-content:center}
  .side-image{width:190px;height:200px;margin-top:14px;background:linear-gradient(135deg,#fafafa,#d9dadc)}
  .categories{margin-top:14px;position:relative}
  .categories h3{font-size:9px;font-weight:700;letter-spacing:1px;color:#555}
  .categories ul{list-style:none;margin-top:5px}
  .categories li{font-size:10px;line-height:13px;color:#555;display:flex;align-items:center;gap:5px}
  .categories li::before{content:"";width:6px;height:6px;border:1px solid #999;border-radius:50%}
  .baby-art{position:absolute;right:-8px;top:22px;width:78px;height:110px;background:linear-gradient(180deg,#8fd0ee,#5ab8e3);border-radius:40px 40px 14px 14px}
</style>
</head>
<body>
<main class="site">
  <header>
    <div class="brand">
      <span class="brand-dot"></span>
      <div>
        <div class="brand-name">Dawnlight</div>
        <div class="brand-sub">MIDWIFERY</div>
      </div>
    </div>
    <div class="social" aria-label="Social links"><span></span><span></span><span></span><span></span></div>
    <nav class="nav">
      <span class="active">Home</span><span>About Us</span><span>Categories</span><span>Your Questions</span><span>Resources</span>
      <span class="contact">
        <svg width="11" height="8" viewBox="0 0 11 8"><rect x="0" y="0" width="11" height="8" fill="#555"/><path d="M0 0 L5.5 4.5 L11 0" stroke="#fff" fill="none"/></svg>
        Contact Us
      </span>
    </nav>
  </header>

  <section class="hero">
    <div class="hero-photo" role="img" aria-label="Family portrait of parents with five children on a white backdrop"></div>
    <blockquote class="hero-quote">
      <p>Motherhood is a dream. It really is absolutely amazing.</p>
      <cite>&ldquo; Marisol Quent</cite>
    </blockquote>
  </section>

  <article class="post post-one">
    <h2 class="post-title">I just love motherhood!</h2>
    <div class="post-meta"><span>Author: Nora Pell</span><span>Date: Wednesday, March 5, 2015</span><span>Comments: 2</span></div>
    <p class="post-body">Welcoming a new baby changes everything, and every family meets that change in its own way. Here I share small moments from the ward, the quiet questions mothers ask at night, and the simple things that help the first weeks feel calmer. Bring your worries, your stories and your hopes; this is a place to rest, read and feel supported while you grow into the parent you already are. <a href="#">Read more &raquo;</a></p>
  </article>

  <div class="gallery">
    <div class="g1" role="img" aria-label="Woman walking along the seashore"></div>
    <div class="g2" role="img" aria-label="Couple embracing by the sea"></div>
    <div class="g3" role="img" aria-label="Red rose held behind a back"></div>
  </div>

  <article class="post post-two">
    <h2 class="post-title">Women should live for love.</h2>
    <div class="post-meta"><span>Author: Ida Fenn</span><span>Date: Monday, March 3, 2015</span><span>Comments: 1</span></div>
    <p class="post-body">Love carries us through pregnancy, labour and the long nights after. In this post we talk about caring for yourself, leaning on the people around you, and keeping room for joy even when days are tiring. Small kindnesses matter, and so does asking for help when you need it most.</p>
  </article>

  <aside class="sidebar">
    <div class="search">
      <div class="search-field">Search</div>
      <div class="search-btn"><svg width="12" height="12" viewBox="0 0 12 12"><circle cx="5" cy="5" r="3.5" stroke="#fff" stroke-width="1.6" fill="none"/><line x1="7.6" y1="7.6" x2="11" y2="11" stroke="#fff" stroke-width="1.8"/></svg></div>
    </div>
    <div class="side-image" role="img" aria-label="Stationery card with pen and eraser on a desk"></div>
    <div class="categories">
      <h3>CATEGORIES</h3>
      <ul>
        <li>Baby</li><li>Help for your child</li><li>Hot Topics</li><li>MOD</li><li>Mommy</li><li>Photos</li><li>Planning for Baby</li><li>Pregnancy</li><li>Prematurity</li><li>Uncategorized</li>
      </ul>
      <div class="baby-art" role="img" aria-label="Light blue baby illustration"></div>
    </div>
  </aside>
</main>
</body>
</html>
```